Business card design Needed for new logo / Construction business, home extensions and new builds

We need a business card design using our new logo files which i will attach to this project :)

We are a small construction business specialising in home extensions, new builds and property development. We are very ambitious and would appreciate professional and elegant designs for our new business card.

Very serious about using the services on BriefNest and recently acquired our new logo from here :)

Please get involved, i will feedback when i can as i am very busy but can respond daily, thanks

Target Market(s)

People that want to build onto their houses, new building developments or adding too their existing property

Industry/Entity Type

Construction

Contact Information for Business Card

Hollin Marsh Construction, Tobias Renwick (Managing Director), Tel 07822200444, email - info@hollin-marsh, www.hollin-marsh.co.uk

Colors

Designer to choose colors to be used in the design.

Requirements
Must have
• I like a deep grey on the back please. A lot of you have provided black from and back, try mixing things up a little. The black looks cool 😎 Thanks

```html
<!DOCTYPE html>
<html lang="en">
<head>
<meta charset="utf-8">
<title>Hollin Marsh Construction – Business Card</title>
<link rel="stylesheet" href="https://fonts.googleapis.com/css2?family=Arimo:wght@400;700&display=swap">
<style>
  :root {
    --backdrop: #d9d9d9;
    --card-front: #1f1f1f;
    --card-back: #3a3a3b;
    --gold: #e9c45c;
    --name: #e4eef2;
    --rule: #c9a640;
  }
  * { margin: 0; padding: 0; box-sizing: border-box; }
  html, body {
    width: 1200px;
    height: 1000px;
    overflow: hidden;
    background: var(--backdrop);
    font-family: "Arimo", Arial, sans-serif;
  }
  .canvas { position: relative; width: 1200px; height: 1000px; }
  .card {
    position: absolute;
    width: 560px;
    height: 362px;
    box-shadow: 0 6px 18px rgba(0,0,0,0.25);
  }
  .card--front { left: 120px; top: 110px; background: var(--card-front); }
  .card--back { left: 520px; top: 530px; background: var(--card-back); }

  /* Front */
  .brand {
    position: absolute;
    left: 0; right: 0; top: 50%;
    transform: translateY(-50%);
    display: flex;
    flex-direction: column;
    align-items: center;
    gap: 18px;
  }
  .brand__square { width: 44px; height: 44px; background: var(--gold); }
  .brand__name {
    color: var(--gold);
    font-weight: 400;
    font-size: 24px;
    letter-spacing: 3px;
    text-transform: uppercase;
    text-align: center;
    line-height: 1.35;
  }

  /* Back */
  .back-brand {
    position: absolute;
    left: 0; top: 0;
    width: 205px; height: 100%;
    display: flex;
    flex-direction: column;
    align-items: center;
    justify-content: center;
    gap: 12px;
  }
  .back-brand__square { width: 30px; height: 30px; background: var(--gold); }
  .back-brand__name {
    color: var(--gold);
    font-size: 14px;
    letter-spacing: 2px;
    text-transform: uppercase;
    text-align: center;
    line-height: 1.4;
  }
  .divider {
    position: absolute;
    left: 205px; top: 30px;
    width: 1px; height: 302px;
    background: var(--rule);
  }
  .details { position: absolute; left: 238px; top: 38px; right: 20px; color: var(--gold); font-size: 16px; }
  .person__name { color: var(--name); font-weight: 700; font-size: 22px; line-height: 1.1; }
  .person__role { font-size: 15px; letter-spacing: 0.5px; text-transform: uppercase; margin-top: 2px; }
  .contact { margin-top: 44px; display: flex; flex-direction: column; gap: 4px; }
  .contact__row { display: flex; align-items: flex-start; gap: 10px; line-height: 1.3; }
  .contact__icon { width: 14px; height: 14px; flex: none; margin-top: 3px; }
  .address { margin-top: 34px; }
</style>
</head>
<body>
<main class="canvas">
  <section class="card card--front" aria-label="Business card front">
    <div class="brand">
      <span class="brand__square"></span>
      <p class="brand__name">Hollin Marsh<br>Construction</p>
    </div>
  </section>

  <section class="card card--back" aria-label="Business card back">
    <div class="back-brand">
      <span class="back-brand__square"></span>
      <p class="back-brand__name">Hollin Marsh<br>Construction</p>
    </div>
    <div class="divider"></div>
    <div class="details">
      <p class="person__name">Tobias Renwick</p>
      <p class="person__role">Managing Director</p>

      <div class="contact">
        <p class="contact__row">
          <svg class="contact__icon" viewBox="0 0 24 24" fill="var(--gold)" aria-hidden="true"><path d="M6.6 10.8a15.1 15.1 0 0 0 6.6 6.6l2.2-2.2a1 1 0 0 1 1-.25 11.4 11.4 0 0 0 3.6.57 1 1 0 0 1 1 1V20a1 1 0 0 1-1 1A17 17 0 0 1 3 4a1 1 0 0 1 1-1h3.5a1 1 0 0 1 1 1c0 1.25.2 2.45.57 3.57a1 1 0 0 1-.25 1z"/></svg>
          <span>+44 7822 200 444</span>
        </p>
        <p class="contact__row">
          <svg class="contact__icon" viewBox="0 0 24 24" fill="var(--gold)" aria-hidden="true"><path d="M2 5h20v14H2z M2 5l10 8 10-8" stroke="var(--card-back)" stroke-width="1.6"/></svg>
          <span>info@hollin-marsh.co.uk</span>
        </p>
      </div>

      <div class="contact address">
        <p class="contact__row">
          <svg class="contact__icon" viewBox="0 0 24 24" fill="var(--gold)" aria-hidden="true"><path d="M12 2a7 7 0 0 0-7 7c0 5 7 13 7 13s7-8 7-13a7 7 0 0 0-7-7zm0 9.5A2.5 2.5 0 1 1 12 6.5a2.5 2.5 0 0 1 0 5z"/></svg>
          <span>Wrenfield Road<br>Larkmoor<br>Dunmere, DM4 6RT</span>
        </p>
      </div>
    </div>
  </section>
</main>
</body>
</html>
```